Webdesign für Steuerberaterin
Zielgruppe
Ich bin Steuerberaterin. Meine Zielgruppe sind sowohl Privatpersonen als auch Unternehmer sowie Männer und Frauen.
Aufgabenstellung
Bitte mein Logo und Foto mit berücksichtigen. Ich möchte keine Website, auf der alle 'Reiter' als eine Seite von oben nach unten durchlaufen. Sondern wirklich einzelne, voneinander getrennte Seiten.

```html
<!DOCTYPE html>
<html lang="de">
<head>
<meta charset="utf-8">
<title>Sabine Hortmann – Steuerberaterin</title>
<link rel="stylesheet" href="https://fonts.googleapis.com/css2?family=PT+Sans:wght@400;700&family=Tinos&family=Open+Sans:wght@400;700&display=swap">
<style>
  :root {
    --sidebar: #1f262e;
    --sidebar-deep: #000000;
    --page: #ffffff;
    --gold: #c49a3a;
    --gold-heading: #a8852a;
    --gold-rule: #c9a53a;
    --footer: #dcb83a;
    --text: #4a4a4a;
    --footer-text: #2b2b2b;
  }
  * { margin: 0; padding: 0; box-sizing: border-box; }
  html, body {
    width: 1200px; height: 768px; overflow: hidden;
    background: var(--page);
  }
  .site { position: relative; width: 1200px; height: 768px; }

  .sidebar {
    position: absolute; left: 0; top: 0;
    width: 307px; height: 473px;
    background: var(--sidebar);
  }
  .sidebar-base {
    position: absolute; left: 0; top: 473px;
    width: 305px; height: 270px;
    background: var(--sidebar-deep);
  }
  .main-nav {
    position: absolute; left: 80px; top: 184px;
    list-style: none;
    font-family: "PT Sans", sans-serif;
    font-size: 13px;
  }
  .main-nav li { position: absolute; left: 0; white-space: nowrap; }
  .main-nav a { color: var(--gold); text-decoration: none; }
  .main-nav .nav-about { top: 0; }
  .main-nav .nav-services { top: 44px; left: 1px; }
  .main-nav .nav-contact { top: 91px; }

  .brand {
    position: absolute; left: 342px; top: 108px;
    width: 200px; text-align: center;
  }
  .brand-name {
    font-family: "Tinos", serif;
    font-size: 24px; color: var(--gold);
    display: block; line-height: 1;
  }
  .brand-title {
    font-family: "Tinos", serif;
    font-size: 7.5px; letter-spacing: 2.6px;
    color: #3a3a3a; display: block; margin-top: 10px;
  }

  .portrait {
    position: absolute; left: 194px; top: 236px;
    width: 457px; height: 332px;
    background: radial-gradient(ellipse at 55% 45%, #fafafa 0%, #e6e6e6 55%, #c9c9c9 100%);
  }

  .welcome {
    position: absolute; left: 693px; top: 0;
    width: 475px;
    text-align: center;
  }
  .welcome-title {
    position: absolute; left: 0; top: 186px; width: 100%;
    font-family: "Tinos", serif; font-weight: 400;
    font-size: 24px; color: var(--gold-heading);
  }
  .welcome-rule {
    position: absolute; left: 0; top: 238px;
    width: 475px; height: 2px; background: var(--gold-rule);
  }
  .welcome-lead {
    position: absolute; left: 0; top: 275px; width: 100%;
    font-family: "Open Sans", sans-serif; font-weight: 700;
    font-size: 13.5px; color: var(--text);
  }
  .welcome-text {
    position: absolute; left: 0; width: 100%;
    font-family: "Open Sans", sans-serif;
    font-size: 13px; line-height: 18px; color: var(--text);
  }
  .p-one { top: 314px; }
  .p-two { top: 424px; }
  .p-three { top: 498px; }

  .site-footer {
    position: absolute; left: 0; top: 743px;
    width: 1200px; height: 25px;
    background: var(--footer);
    font-family: "PT Sans", sans-serif;
    font-size: 13px; color: var(--footer-text);
    padding-left: 81px; line-height: 25px;
  }
  .site-footer a { color: var(--footer-text); text-decoration: none; }
  .site-footer .sep { margin: 0 8px; }
</style>
</head>
<body>
<div class="site">
  <aside class="sidebar">
    <ul class="main-nav">
      <li class="nav-about"><a href="#">Über mich</a></li>
      <li class="nav-services"><a href="#">Leistungen</a></li>
      <li class="nav-contact"><a href="#">Kontakt</a></li>
    </ul>
  </aside>
  <div class="sidebar-base"></div>

  <div class="brand">
    <span class="brand-name">Sabine Hortmann</span>
    <span class="brand-title">STEUERBERATERIN</span>
  </div>

  <div class="portrait" role="img" aria-label="Porträtfoto der Steuerberaterin vor heller Steinwand"></div>

  <section class="welcome">
    <h1 class="welcome-title">Schön, dass Sie da sind</h1>
    <div class="welcome-rule"></div>
    <p class="welcome-lead">Ich freue mich, dass Sie den Weg zu mir gefunden haben!</p>
    <p class="welcome-text p-one">Sie sind bei mir genau richtig:<br>Egal, ob Sie Privatperson sind, die Ihre Einkommensteuer-Erklärung<br>in vertrauensvolle Hände geben möchte,<br>oder Unternehmer, der sich z.B. das „Rundum-Sorglos-Paket“<br>mit Buchführung, Jahresabschluss und Steuererklärungen wünscht.</p>
    <p class="welcome-text p-two">Schauen Sie sich hier gerne um und melden Sie sich bei mir<br>– ich bin bei jedem steuerlichen Thema<br>gerne Ihr kompetenter und zuverlässiger Ansprechpartner.</p>
    <p class="welcome-text p-three">Für mich ist es eine Selbstverständlichkeit,<br>dass ich auch nach mehr als 12 Jahren Berufserfahrung<br>durch permanente Fortbildungen immer auf dem aktuellsten Stand<br>der relevanten Gesetze und Verordnungen bin.<br>Nur so kann ich Sie bestmöglich beraten.</p>
  </section>

  <footer class="site-footer">
    <a href="#">Impressum</a><span class="sep">|</span><a href="#">Datenschutz</a>
  </footer>
</div>
</body>
</html>
```